Website for Fashion/Jewelry online seller

We would like a website design that can be used in wordpress. It will be important to be able to link instagram, twitter, etc posts on the bottom of site. We are to be a online seller of chic jewelry, art, fashion, and other home design industries. Currently we emphasize jewelry but as the years move forward, other products will be introduced as collections in home furnishings and primarily women's fashion. It will be important to have a “shop now” section where people can order products online so ecommerce will need to be set up at some point. The website should have the following feel: clean, modern, contemporary and chic. A lot of whites should be used with simple text and simple but elegant fonts. Best is to go to mirevantello.com to get the best idea of what we are wanting for the look and feel of the site.

Target Market(s)

upper social class people that are into fashion, jewelry, etc

Industry/Entity Type

Fashion

Number of Pages Required

5+ page

Font styles to use
Other font styles liked:
• go to daskorvin.com to see the font desired

Requirements
Must have
• Name of Company is Tide Hollow 7
Nice to have
• see project description
Should not have
• see project description

```html
<!DOCTYPE html>
<html lang="en">
<head>
<meta charset="utf-8">
<title>Tide Hollow 7 — Shop</title>
<link href="https://fonts.googleapis.com/css2?family=Dosis:wght@300;400;500;600;700&family=Playball&display=swap" rel="stylesheet">
<style>
  :root{
    --orange:#ff7a0d;
    --ink:#1c1c1c;
    --white:#ffffff;
    --footer:#2c2c2c;
    --footer-mid:#222222;
    --footer-text:#d0d0d0;
    --muted:#8a8a8a;
    --panel:rgba(118,112,114,.62);
    --bracket:#d9d9d9;
  }
  *{box-sizing:border-box;margin:0;padding:0}
  html,body{width:1200px;height:1015px;overflow:hidden;background:var(--white)}
  body{position:relative;font-family:"Dosis",sans-serif;color:var(--ink)}
  a{color:inherit;text-decoration:none}

  .frame-top{position:absolute;left:0;top:0;width:1200px;height:3px;background:var(--orange);z-index:5}
  .frame-left{position:absolute;left:0;top:0;width:3px;height:1015px;background:var(--orange);z-index:5}

  .hero-photo{position:absolute;left:0;top:0;width:1200px;height:826px;
    background:
      radial-gradient(ellipse 230px 330px at 650px 330px, #c9a48a 0%, rgba(201,164,138,0) 100%),
      linear-gradient(180deg,#ebe9e6 0%,#e4e0dc 45%,#3a3850 70%,#2e2c44 100%)}

  .sidebar{position:absolute;left:0;top:0;width:210px;height:975px;background:rgba(255,255,255,.86);z-index:2}
  .account-nav{position:absolute;top:34px;left:0;width:206px;list-style:none;text-align:center}
  .account-nav li{height:24.3px;font-size:12px;font-weight:600;letter-spacing:.2px;line-height:16px}
  .brand{position:absolute;left:13px;top:196px;font-size:28px;font-weight:700;color:var(--orange);letter-spacing:.2px;white-space:nowrap}
  .main-nav{position:absolute;top:279px;left:0;width:206px;list-style:none;text-align:center}
  .main-nav li{height:28.7px;font-size:13px;font-weight:600;line-height:22px}
  .main-nav .active a{display:inline-block;border:2px solid var(--orange);color:var(--orange);padding:0 8px;line-height:19px;font-weight:500}

  .cart{position:absolute;left:1106px;top:3px;width:94px;height:27px;background:var(--orange);color:var(--white);
    font-size:12px;font-weight:500;display:flex;align-items:center;justify-content:center;gap:4px;z-index:3}

  .slide-panel{position:absolute;left:394px;top:251px;width:617px;height:323px;background:var(--panel);text-align:center;color:var(--white)}
  .slide-panel .corners{position:absolute;left:0;top:0}
  .eyebrow{position:absolute;top:26px;left:0;width:100%;font-size:26px;font-weight:600;letter-spacing:4px}
  .headline{position:absolute;top:60px;left:0;width:100%;font-family:"Playball",cursive;font-size:76px;line-height:1;font-weight:400}
  .lede{position:absolute;top:176px;left:0;width:100%;font-size:14px;font-weight:300;line-height:20px}
  .shop-now{position:absolute;left:250px;top:252px;width:150px;height:42px;background:var(--orange);color:var(--white);
    font-size:22px;font-weight:700;letter-spacing:3px;line-height:42px}

  .slide-arrow{position:absolute;top:386px;width:20px;height:56px;background:var(--ink);color:var(--white);
    font-size:8px;font-weight:600;line-height:10px;text-align:center;display:flex;flex-direction:column;justify-content:center}
  .slide-arrow.prev{left:351px}
  .slide-arrow.next{left:1037px}

  .site-footer{position:absolute;left:210px;top:826px;width:990px;height:149px;display:flex}
  .footer-col{position:relative;height:149px;color:var(--footer-text)}
  .footer-col h2{font-size:21px;font-weight:700;color:var(--orange);letter-spacing:.3px;line-height:24px}
  .contact-col{width:356px;background:var(--footer);padding:24px 0 0 41px}
  .contact-col ul{list-style:none;margin-top:13px;font-size:12.5px;font-weight:300}
  .contact-col li{height:22px;display:flex;align-items:center;gap:5px}
  .contact-col .email{color:var(--orange)}
  .connect-col{width:306px;background:var(--footer-mid);padding-top:24px;text-align:center}
  .connect-col p,.newsletter-col p{margin-top:10px;font-size:12.5px;font-weight:300}
  .social{display:flex;gap:14px;justify-content:center;margin-top:10px;list-style:none}
  .social li{width:32px;height:32px;border:1px solid #3a3a3a;display:flex;align-items:center;justify-content:center}
  .newsletter-col{width:328px;background:var(--footer);padding:24px 30px 0 0;text-align:right}
  .signup{display:flex;justify-content:flex-end;margin-top:12px}
  .signup input{width:234px;height:32px;background:transparent;border:1px solid #3a3a3a;border-right:0;padding-left:14px;
    font-family:"Dosis",sans-serif;font-size:10px;color:var(--footer-text)}
  .signup input::placeholder{color:var(--footer-text)}
  .signup button{width:32px;height:32px;border:0;background:var(--orange);display:flex;align-items:center;justify-content:center}
  .col-notch{position:absolute;top:0}

  .bottom-bar{position:absolute;left:210px;top:975px;width:990px;height:40px;background:var(--white)}
  .bottom-nav{position:absolute;left:39px;top:10px;list-style:none;display:flex;font-size:12px;font-weight:500}
  .bottom-nav li+li::before{content:"|";margin:0 16px 0 17px;font-weight:600}
  .bottom-nav .active{color:var(--orange);font-weight:400}
  .copyright{position:absolute;right:28px;top:13px;font-size:12.5px;font-weight:300;color:var(--muted)}
</style>
</head>
<body>
  <div class="frame-top"></div>
  <div class="frame-left"></div>

  <div class="hero-photo" role="img" aria-label="Fashion photograph: a model in sparkling tights seated on a dark bed with an ornate metal frame and a fur throw"></div>

  <aside class="sidebar">
    <ul class="account-nav">
      <li><a href="#">MY ACCOUNT</a></li>
      <li><a href="#">WISHLIST</a></li>
      <li><a href="#">CHECKOUT</a></li>
      <li><a href="#">LOGIN</a></li>
      <li><a href="#">REGISTER</a></li>
    </ul>
    <div class="brand">TIDE HOLLOW 7</div>
    <ul class="main-nav">
      <li class="active"><a href="#">SHOP</a></li>
      <li><a href="#">ABOUT</a></li>
      <li><a href="#">CHARITY</a></li>
      <li><a href="#">LOCATIONS</a></li>
      <li><a href="#">CONTACT</a></li>
    </ul>
  </aside>

  <a class="cart" href="#">
    <svg width="14" height="12" viewBox="0 0 14 12" aria-hidden="true"><path d="M0 1h2.5l2 7h7l1.5-5H4" fill="none" stroke="#fff" stroke-width="1.6"/><circle cx="5.5" cy="10.5" r="1.2" fill="#fff"/><circle cx="10.5" cy="10.5" r="1.2" fill="#fff"/></svg>
    CART(12)
    <svg width="8" height="5" viewBox="0 0 8 5" aria-hidden="true"><path d="M0 0h8L4 5z" fill="#fff"/></svg>
  </a>

  <section class="slide-panel">
    <svg class="corners" width="617" height="323" aria-hidden="true">
      <g fill="none" stroke="var(--bracket)" stroke-width="4">
        <path d="M8 54V8h48"/><path d="M561 8h48v46"/>
        <path d="M8 269v46h48"/><path d="M561 315h48v-46"/>
      </g>
    </svg>
    <div class="eyebrow">NEW TREND</div>
    <h1 class="headline">Huge Collection</h1>
    <p class="lede">Lorem ipsum dolor sit amet, consectetuer adipiscing elit, sed diam nonummy<br>nibh euismod tincidunt ut laoreet dolore magna aliquam erat volutpat.</p>
    <a class="shop-now" href="#">SHOP NOW</a>
  </section>

  <a class="slide-arrow prev" href="#"><span>P</span><span>R</span><span>E</span><span>V</span></a>
  <a class="slide-arrow next" href="#"><span>N</span><span>E</span><span>X</span><span>T</span></a>

  <footer class="site-footer">
    <div class="footer-col contact-col">
      <h2>CONTACT US</h2>
      <ul>
        <li><svg width="8" height="10" viewBox="0 0 8 10" aria-hidden="true"><path d="M4 9.5S.7 5.8.7 3.6a3.3 3.3 0 0 1 6.6 0C7.3 5.8 4 9.5 4 9.5z" fill="none" stroke="#d0d0d0"/><circle cx="4" cy="3.6" r="1.1" fill="#d0d0d0"/></svg>D - 118, Marlow building, East Harbor</li>
        <li><svg width="9" height="9" viewBox="0 0 9 9" aria-hidden="true"><path d="M1.5.8l1.6 1.8-.8 1.3a5 5 0 0 0 2.8 2.8l1.3-.8 1.8 1.6-1 1.1C4.6 8.6.4 4.4.4 1.8z" fill="none" stroke="#d0d0d0" stroke-width=".9"/></svg>(+222) 555 0142 318</li>
        <li><svg width="9" height="7" viewBox="0 0 9 7" aria-hidden="true"><rect x=".5" y=".5" width="8" height="6" fill="none" stroke="#d0d0d0"/><path d="M.5.5l4 3.5 4-3.5" fill="none" stroke="#d0d0d0"/></svg><span class="email">contact@tidehollow7.com</span></li>
      </ul>
    </div>
    <div class="footer-col connect-col">
      <svg class="col-notch" style="left:-28px" width="28" height="24" aria-hidden="true"><path d="M0 1.5h26.5V24" fill="none" stroke="#555" stroke-width="3"/></svg>
      <h2>CONNECT WITH US</h2>
      <p>Join the conversion about Tide Hollow 7</p>
      <ul class="social">
        <li aria-label="Social link one"><svg width="8" height="8" aria-hidden="true"><circle cx="4" cy="4" r="3" fill="none" stroke="#d0d0d0"/></svg></li>
        <li aria-label="Social link two"><svg width="8" height="8" aria-hidden="true"><circle cx="4" cy="4" r="3" fill="none" stroke="#d0d0d0"/></svg></li>
        <li aria-label="Social link three"><svg width="8" height="8" aria-hidden="true"><circle cx="4" cy="4" r="3" fill="none" stroke="#d0d0d0"/></svg></li>
        <li aria-label="Social link four"><svg width="8" height="8" aria-hidden="true"><circle cx="4" cy="4" r="3" fill="none" stroke="#d0d0d0"/></svg></li>
        <li aria-label="Social link five"><svg width="8" height="8" aria-hidden="true"><circle cx="4" cy="4" r="3" fill="none" stroke="#d0d0d0"/></svg></li>
      </ul>
    </div>
    <div class="footer-col newsletter-col">
      <svg class="col-notch" style="left:0" width="28" height="24" aria-hidden="true"><path d="M1.5 24V1.5H28" fill="none" stroke="#555" stroke-width="3"/></svg>
      <h2>NEWSLETTER</h2>
      <p>Lorem ipsum dolor sit consectetuer adipiscing elit</p>
      <form class="signup">
        <input type="email" placeholder="Your email address...">
        <button type="button" aria-label="Subscribe"><svg width="12" height="10" viewBox="0 0 12 10" aria-hidden="true"><path d="M0 5h10M6 1l4 4-4 4" fill="none" stroke="#fff" stroke-width="2"/></svg></button>
      </form>
    </div>
  </footer>

  <div class="bottom-bar">
    <ul class="bottom-nav">
      <li class="active"><a href="#">SHOP</a></li>
      <li><a href="#">ABOUT</a></li>
      <li><a href="#">CHARITY</a></li>
      <li><a href="#">LOCATIONS</a></li>
      <li><a href="#">CONTACT</a></li>
    </ul>
    <p class="copyright">All rights reserved. © 2016 Tide Hollow 7</p>
  </div>
</body>
</html>
```